Emmy award winning Hollywood sound studio needs a cool website

We need a website designed and coded to showcase our company and talent to our current and future clients. We are a post-production sound studio that works with Brambletoon, Vidora, Calder Sisters, Glimmerforge, and other major Hollywood studios and companies. We primarily work designing sound effects for animated TV shows like Puddlefin McGee, Rookie Rangers Roll!, Tiger Dojo: Lantern Riders, Fossil Valley Stampede Files, The Sly Crew, My Aunt the Starship Pilot, Spear of Helix, and the recent Vidora movie Wren and the Quiet. A website for our company would provide basic information about our studio and services, the kinds of projects we are currently working on and have worked on in the past, the awards we have won or been nominated for, and most importantly showcase our talented engineers so that producers and directors can get to know the people they might want to collaborate with. Our studio is located in Burbank, CA right in the heart of where all the studios are located. We have a basic company logo. We don't really have a color scheme to our studio so we're very open and flexible in that department. We have decorated our studio with a bit of an Art Deco style to invoke an old classy movie theater from the golden age of Hollywood. Our lobby resembles the lobby of a movie theater complete with a neon marquee where we post fun sayings or quotes from our shows. I think it would be fun for the website design to reflect that Art Deco/classic movie theater feeling. Another website that I think has a good simple design for inspiration is Fernhollow Audio: "www.fernaudio.example".
Target Market(s)
Major Hollywood Studios, Animation production companies, independent film/TV production
Industry/Entity Type
Hollywood, Television, Streaming, Entertainment, Games
Coding
Coded - Design and coding required
Number of Pages Required
5+ page
Look and feel

```html
<!DOCTYPE html>
<html lang="en">
<head>
<meta charset="utf-8">
<title>Reelhouse Audio — Post-Production Sound Studio</title>
<link href="https://fonts.googleapis.com/css2?family=Poppins:wght@400;500;600;700;800&display=swap" rel="stylesheet">
<style>
:root{
  --bg:#1b1b1b;
  --footer:#0b0b0b;
  --card:#0d0d0d;
  --white:#ffffff;
  --text:#e6e6e6;
  --muted:#b5b5b5;
  --blue:#16a3e0;
  --navy:#0c2f57;
  --rule:#5a5a5a;
  --band:#2c2c2c;
  --band-line:#6a6a6a;
}
*{margin:0;padding:0;box-sizing:border-box}
html,body{width:1200px;height:5352px;overflow:hidden}
body{background:var(--bg);color:var(--text);font-family:'Poppins',sans-serif;position:relative}
.abs{position:absolute}
.divider{position:absolute;left:0;width:1200px;height:24px;background:var(--band);border-top:2px solid var(--band-line);border-bottom:2px solid var(--band-line)}
.divider::after{content:"";position:absolute;left:0;right:0;top:9px;height:2px;background:var(--band-line)}
.btn{position:absolute;height:44px;border-radius:22px;background:var(--white);color:#111;font-size:12px;font-weight:600;display:flex;align-items:center;justify-content:center}
h2.section-title{position:absolute;left:0;width:1200px;text-align:center;color:var(--white);font-weight:700;font-size:40px;line-height:1}
.eyebrow{position:absolute;left:0;width:1200px;text-align:center;font-size:13px;color:#8a8a8a;letter-spacing:1px}

/* header */
.topbar{top:6px;right:126px;font-size:13px;color:var(--white);display:flex;gap:26px}
.logo{top:30px;left:112px;width:170px;font-weight:800;font-size:25px;line-height:27px;color:var(--white);letter-spacing:1px}
.nav{top:64px;left:462px;display:flex;gap:28px;font-size:14px;font-weight:600;color:var(--white)}

/* hero */
.hero{top:141px;left:0;width:1200px;height:545px;background:linear-gradient(180deg,#0d0d0d,#1b1b1b)}
.hero-rule{top:154px;left:112px;width:978px;height:6px;background:#7a6f6a}
.hero-art{top:170px;left:480px;width:660px;height:500px;background:
  radial-gradient(ellipse 30% 38% at 50% 42%,#0e0f14 0%,#0e0f14 55%,transparent 70%),
  radial-gradient(ellipse 48% 46% at 50% 45%,#2a8bb0 0%,#1d5f86 40%,#173450 62%,transparent 78%),
  radial-gradient(ellipse 60% 22% at 50% 70%,rgba(120,200,240,.35),transparent 70%)}
.hero-title{top:244px;left:112px;color:var(--white);font-weight:800;line-height:1}
.hero-title .outline{display:block;font-size:76px;color:transparent;-webkit-text-stroke:2px var(--white);font-weight:600}
.hero-title .solid{display:block;font-size:80px;margin-top:4px}
.hero-copy{top:434px;left:112px;width:430px;font-size:12.5px;line-height:24px;color:var(--white)}

/* studio */
.studio-copy{top:788px;left:245px;width:710px;text-align:center;font-size:15.5px;line-height:26px;color:var(--text)}
.studio-copy p+p{margin-top:26px}

/* posters */
.poster{position:absolute;background:var(--white);border-radius:4px;padding:14px}
.poster .art{width:100%;height:100%;border-radius:2px}
.poster-cap{position:absolute;text-align:center;font-size:11.5px;line-height:15px;color:var(--muted)}
.poster-cap b{display:block;color:var(--white);font-weight:600;font-size:12px}
.arrow{position:absolute;width:28px;height:28px;border-radius:50%;background:var(--white);display:flex;align-items:center;justify-content:center}

/* services */
.service{position:absolute;width:295px;height:484px;background:var(--card);border-radius:4px}
.service .art{position:absolute;top:12px;left:12px;width:271px;height:224px}
.service .icon{position:absolute;top:196px;left:107px;width:80px;height:80px;border-radius:50%;background:var(--card);border:4px solid var(--white);display:flex;align-items:center;justify-content:center}
.service h3{position:absolute;top:298px;left:0;width:295px;text-align:center;color:var(--white);font-size:15px;font-weight:600}
.service p{position:absolute;top:330px;left:30px;width:235px;text-align:center;font-size:14px;line-height:25px;color:var(--text)}
.service .pill{position:absolute;top:408px;left:74px;width:146px;height:44px;border-radius:22px;background:#3a3a3a;color:var(--white);font-size:12px;display:flex;align-items:center;justify-content:center}

/* team */
.member{position:absolute;width:232px;height:303px;background:#0f0f0f;border-radius:4px}
.member .art{position:absolute;top:12px;left:12px;width:208px;height:187px}
.member h4{position:absolute;top:222px;left:0;width:100%;text-align:center;color:var(--white);font-size:15px;font-weight:600}
.member p{position:absolute;top:250px;left:20px;right:20px;text-align:center;font-size:12.5px;line-height:16px;color:var(--muted)}

/* awards */
.awards-label{top:4112px;left:104px;font-size:14px;color:var(--muted);letter-spacing:.5px}
.awards-title{top:4132px;left:104px;font-size:34px;font-weight:700;color:var(--white)}
.awards-copy{top:4116px;left:463px;width:610px;font-size:14px;line-height:25px;color:var(--text)}
.award-row{position:absolute;left:463px;width:622px;height:68px;border-bottom:1px solid var(--rule);font-size:15.5px;color:var(--white);font-weight:500}
.award-row span{position:absolute;top:20px}

/* contact */
.contact-title{top:4606px;left:104px;width:400px;font-size:26px;line-height:31px;font-weight:600;color:var(--white)}
.contact-copy{top:4684px;left:104px;width:430px;font-size:13.5px;line-height:26px;color:var(--text)}
.form-box{top:4550px;left:596px;width:499px;height:447px;background:var(--blue)}
.form-box h3{position:absolute;top:24px;left:0;width:100%;text-align:center;font-size:38px;font-weight:700;color:#0b1f33}
.field{position:absolute;border:1.5px solid rgba(255,255,255,.85);font-size:12.5px;font-weight:500;color:var(--white);padding:10px 12px}
.submit{position:absolute;top:376px;left:169px;width:180px;height:46px;border-radius:23px;background:var(--navy);color:var(--white);font-size:12.5px;font-weight:600;display:flex;align-items:center;justify-content:center}

/* footer */
.footer{top:4915px;left:0;width:1200px;height:437px;background:var(--footer)}
.foot-tag{top:5050px;left:102px;font-size:32px;line-height:38px;font-weight:700;color:var(--white)}
.vrule{top:5028px;width:1px;height:218px;background:#333}
.foot-h{font-size:14px;font-weight:600;color:var(--white)}
.foot-t{font-size:13.5px;line-height:23px;color:var(--text)}
.foot-nav{top:5294px;left:102px;display:flex;font-size:11px;color:var(--muted)}
.foot-nav span{padding:0 12px;border-right:1px solid #666}
.foot-nav span:first-child{padding-left:0}
.foot-nav span:last-child{border:none}
.copyright{top:5294px;left:750px;font-size:11px;color:var(--muted)}
.to-top{top:5288px;left:1058px;width:28px;height:28px;border-radius:50%;background:var(--blue);display:flex;align-items:center;justify-content:center}
</style>
</head>
<body>

<!-- Header -->
<div class="abs topbar">
  <span>&#9742; 555-014-2290</span>
  <span>&#10148; hello@reelhouseaudio.example</span>
</div>
<div class="abs logo">REELHOUSE<br>AUDIO</div>
<nav class="abs nav">
  <span>HOME</span><span>PEOPLE</span><span>SERVICES</span><span>PROJECT</span><span>LATEST</span><span>CONTACT US</span>
</nav>
<div class="divider" style="top:120px"></div>

<!-- Hero -->
<section class="abs hero"></section>
<div class="abs hero-rule"></div>
<div class="abs hero-art" role="img" aria-label="Studio headphones surrounded by flowing blue sound waves"></div>
<h1 class="abs hero-title"><span class="outline">Audio</span><span class="solid">Mastering</span></h1>
<p class="abs hero-copy">Lorem Ipsum is simply dummy text of the printing and typesetting industry. Lorem Ipsum has been the industry's standard</p>
<div class="btn" style="top:519px;left:112px;width:185px">Read More</div>

<!-- Our Studio -->
<h2 class="section-title" style="top:732px">OUR STUDIO</h2>
<div class="abs studio-copy">
  <p>Lorem Ipsum is simply dummy text of the printing and typesetting industry. Lorem Ipsum has been the industry's standard dummy</p>
  <p>text ever since the 1500s, when an unknown printer took a galley of type and scrambled it to make a type specimen book. It has survived not only five centuries, but also the leap into electronic typesetting, remaining essentially unchanged. It was popularised in the 1960s with the release of Letraset sheets containing</p>
</div>
<div class="btn" style="top:1016px;left:509px;width:183px">Read More</div>
<div class="divider" style="top:1123px"></div>

<!-- Latest Projects -->
<h2 class="section-title" style="top:1196px">Latest Projects</h2>
<div class="arrow" style="top:1393px;left:55px"><svg width="10" height="10" viewBox="0 0 10 10"><path d="M6.5 1.5 3 5l3.5 3.5" stroke="#111" stroke-width="1.6" fill="none"/></svg></div>
<div class="arrow" style="top:1393px;left:1100px"><svg width="10" height="10" viewBox="0 0 10 10"><path d="M3.5 1.5 7 5 3.5 8.5" stroke="#111" stroke-width="1.6" fill="none"/></svg></div>

<div class="poster" style="top:1276px;left:104px;width:228px;height:257px"><div class="art" role="img" aria-label="Poster: dinosaur adventure series" style="background:radial-gradient(circle at 35% 35%,#9aa8b2,transparent 55%),radial-gradient(circle at 70% 75%,#b0683a,transparent 60%),linear-gradient(160deg,#5f6f7c,#3a2c20)"></div></div>
<div class="poster" style="top:1276px;left:355px;width:229px;height:257px"><div class="art" role="img" aria-label="Poster: caped hero animated series" style="background:radial-gradient(ellipse at 50% 30%,#5a7aa0,transparent 55%),linear-gradient(180deg,#2c3c55,#0f1522)"></div></div>
<div class="poster" style="top:1276px;left:607px;width:228px;height:257px"><div class="art" role="img" aria-label="Poster: Fossil Valley Stampede Files" style="background:radial-gradient(circle at 50% 40%,#8a5a2a,transparent 55%),radial-gradient(ellipse at 50% 90%,#d09a2a,transparent 50%),linear-gradient(180deg,#2a211a,#4a3420)"></div></div>
<div class="poster" style="top:1276px;left:858px;width:229px;height:257px"><div class="art" role="img" aria-label="Poster: holiday animated movie" style="background:radial-gradient(circle at 50% 25%,#f0d060,transparent 45%),radial-gradient(circle at 40% 80%,#d8483a,transparent 55%),linear-gradient(180deg,#3aa0c8,#2a6a9a)"></div></div>

<div class="poster-cap" style="top:1549px;left:104px;width:228px"><b>HOLLOW HARBOR</b>Ren Okafor<br>Starlit Pictures</div>
<div class="poster-cap" style="top:1549px;left:355px;width:229px"><b>HOLLOW HARBOR</b>Ren Okafor<br>Starlit Pictures</div>
<div class="poster-cap" style="top:1549px;left:607px;width:228px"><b>HOLLOW HARBOR</b>Ren Okafor<br>Starlit Pictures</div>
<div class="poster-cap" style="top:1549px;left:858px;width:229px"><b>HOLLOW HARBOR</b>Ren Okafor<br>Starlit Pictures</div>
<div class="divider" style="top:1656px"></div>

<!-- Services -->
<div class="eyebrow" style="top:1740px">ABOUT MAKING MUSIC</div>
<h2 class="section-title" style="top:1763px">OUR SERVICES FOR YOU</h2>

<div class="service" style="top:1901px;left:108px">
  <div class="art" role="img" aria-label="Engineer recording at a mixing desk" style="background:radial-gradient(circle at 70% 30%,#6aa8c8,transparent 35%),radial-gradient(circle at 30% 45%,#8a8a8a,transparent 45%),linear-gradient(180deg,#4a4a4a,#1a1a1a)"></div>
  <div class="icon"><svg width="34" height="34" viewBox="0 0 34 34"><rect x="3" y="3" width="28" height="28" rx="4" fill="none" stroke="#fff" stroke-width="2"/><path d="M14 24V11l9-2v12" fill="none" stroke="#fff" stroke-width="2"/><circle cx="12" cy="24" r="2.5" fill="#fff"/><circle cx="21" cy="21" r="2.5" fill="#fff"/></svg></div>
  <h3>Re-recording Mixing</h3>
  <p>Make a type specimen book. It has survived not only five centuries, but also the leap</p>
  <div class="pill">Read More</div>
</div>
<div class="service" style="top:1841px;left:445px">
  <div class="art" role="img" aria-label="Close view of mixing console faders" style="background:radial-gradient(ellipse at 60% 30%,#b0b0b0,transparent 50%),linear-gradient(170deg,#7a7a7a,#202020)"></div>
  <div class="icon"><svg width="34" height="34" viewBox="0 0 34 34"><rect x="4" y="6" width="26" height="22" rx="3" fill="none" stroke="#fff" stroke-width="2"/><path d="M9 12h16M9 17h16M9 22h10" stroke="#fff" stroke-width="2"/></svg></div>
  <h3>Sound Design &amp; Editorial</h3>
  <p>Make a type specimen book. It has survived not only five centuries, but also the leap</p>
  <div class="pill">Read More</div>
</div>
<div class="service" style="top:1901px;left:783px">
  <div class="art" role="img" aria-label="Hands on a DJ controller" style="background:radial-gradient(circle at 30% 35%,#c09a80,transparent 40%),radial-gradient(circle at 75% 35%,#a07860,transparent 40%),linear-gradient(180deg,#5a4236,#1c1818)"></div>
  <div class="icon"><svg width="34" height="34" viewBox="0 0 34 34"><rect x="3" y="5" width="28" height="20" rx="3" fill="none" stroke="#fff" stroke-width="2"/><path d="M12 29h10M17 25v4M10 15h4M20 15h4M12 11v8M22 11v8" stroke="#fff" stroke-width="2"/></svg></div>
  <h3>Sound Design And Mix In La</h3>
  <p>Make a type specimen book. It has survived not only five centuries, but also the leap</p>
  <div class="pill">Read More</div>
</div>
<div class="btn" style="top:2381px;left:494px;width:185px">Read More</div>
<div class="divider" style="top:2486px"></div>

<!-- Our Projects -->
<h2 class="section-title" style="top:2574px">Our Projects</h2>

<div class="poster" style="top:2651px;left:104px;width:228px;height:260px"><div class="art" role="img" aria-label="Poster: superhero team series" style="background:radial-gradient(circle at 50% 65%,#5a9a6a,transparent 50%),linear-gradient(180deg,#1f3a3a,#2f5a4a)"></div></div>
<div class="poster" style="top:2651px;left:355px;width:229px;height:260px"><div class="art" role="img" aria-label="Poster: Tiger Dojo: Lantern Riders" style="background:radial-gradient(circle at 40% 40%,#f0c070,transparent 50%),radial-gradient(circle at 75% 70%,#e8e0d8,transparent 35%),linear-gradient(180deg,#c88a4a,#6a3a2a)"></div></div>
<div class="poster" style="top:2651px;left:607px;width:228px;height:260px"><div class="art" role="img" aria-label="Poster: ensemble drama series" style="background:radial-gradient(ellipse at 50% 60%,#d8b8a0,transparent 55%),linear-gradient(180deg,#a8bccb,#8a8a9a)"></div></div>
<div class="poster" style="top:2651px;left:858px;width:229px;height:260px"><div class="art" role="img" aria-label="Poster: preschool adventure series" style="background:radial-gradient(circle at 50% 30%,#f060a0,transparent 40%),radial-gradient(circle at 50% 75%,#60c0e0,transparent 45%),linear-gradient(180deg,#3a5ad8,#6a3ac8)"></div></div>
<div class="poster-cap" style="top:2928px;left:104px;width:228px"><b>HOLLOW HARBOR</b>Ren Okafor<br>Starlit Pictures</div>
<div class="poster-cap" style="top:2928px;left:355px;width:229px"><b>HOLLOW HARBOR</b>Ren Okafor<br>Starlit Pictures</div>
<div class="poster-cap" style="top:2928px;left:607px;width:228px"><b>HOLLOW HARBOR</b>Ren Okafor<br>Starlit Pictures</div>
<div class="poster-cap" style="top:2928px;left:858px;width:229px"><b>HOLLOW HARBOR</b>Ren Okafor<br>Starlit Pictures</div>

<div class="poster" style="top:3025px;left:104px;width:228px;height:260px"><div class="art" role="img" aria-label="Poster: cartoon dog comedy movie" style="background:radial-gradient(circle at 50% 30%,#e8483a,transparent 40%),radial-gradient(circle at 50% 80%,#c89a5a,transparent 45%),linear-gradient(180deg,#f0d070,#5aa0d8)"></div></div>
<div class="poster" style="top:3025px;left:355px;width:229px;height:260px"><div class="art" role="img" aria-label="Poster: space station drama" style="background:radial-gradient(circle at 50% 55%,#b070d0,transparent 45%),linear-gradient(180deg,#4a2a7a,#1a1030)"></div></div>
<div class="poster" style="top:3025px;left:607px;width:228px;height:260px"><div class="art" role="img" aria-label="Poster: animated action series" style="background:radial-gradient(circle at 50% 45%,#7a8ac8,transparent 45%),radial-gradient(ellipse at 50% 90%,#e0a83a,transparent 45%),linear-gradient(180deg,#2a3a7a,#1a2040)"></div></div>
<div class="poster" style="top:3025px;left:858px;width:229px;height:260px"><div class="art" role="img" aria-label="Poster: robot cadets series" style="background:radial-gradient(circle at 45% 45%,#e07a4a,transparent 45%),linear-gradient(180deg,#c8503a,#2a5a8a)"></div></div>
<div class="poster-cap" style="top:3302px;left:104px;width:228px"><b>HOLLOW HARBOR</b>Ren Okafor<br>Starlit Pictures</div>
<div class="poster-cap" style="top:3302px;left:355px;width:229px"><b>HOLLOW HARBOR</b>Ren Okafor<br>Starlit Pictures</div>
<div class="poster-cap" style="top:3302px;left:607px;width:228px"><b>HOLLOW HARBOR</b>Ren Okafor<br>Starlit Pictures</div>
<div class="poster-cap" style="top:3302px;left:858px;width:229px"><b>HOLLOW HARBOR</b>Ren Okafor<br>Starlit Pictures</div>
<div class="btn" style="top:3401px;left:509px;width:183px">View All Projects</div>
<div class="divider" style="top:3512px"></div>

<!-- Team -->
<div class="eyebrow" style="top:3606px;color:var(--muted)">THE WORLD OF MUSIC</div>
<h2 class="section-title" style="top:3635px">The Best Studio in the City</h2>
<div class="arrow" style="top:3852px;left:52px"><svg width="10" height="10" viewBox="0 0 10 10"><path d="M6.5 1.5 3 5l3.5 3.5" stroke="#111" stroke-width="1.6" fill="none"/></svg></div>
<div class="arrow" style="top:3852px;left:1097px"><svg width="10" height="10" viewBox="0 0 10 10"><path d="M3.5 1.5 7 5 3.5 8.5" stroke="#111" stroke-width="1.6" fill="none"/></svg></div>

<div class="member" style="top:3717px;left:100px"><div class="art" role="img" aria-label="Portrait photo of a team member" style="background:radial-gradient(ellipse 40% 55% at 50% 70%,#7a8aa0,transparent 80%),linear-gradient(180deg,#f0b050,#c07a20)"></div><h4>JOHN SMITH</h4><p>Senior Vice President and General Manager</p></div>
<div class="member" style="top:3717px;left:349px"><div class="art" role="img" aria-label="Portrait photo of a team member" style="background:radial-gradient(ellipse 40% 55% at 50% 70%,#2a2a2a,transparent 80%),linear-gradient(180deg,#7a4234,#3a2622)"></div><h4>JOHN SMITH</h4><p>Senior Vice President and General Manager</p></div>
<div class="member" style="top:3717px;left:596px"><div class="art" role="img" aria-label="Portrait photo of a team member" style="background:radial-gradient(ellipse 40% 55% at 50% 70%,#a05a3a,transparent 80%),linear-gradient(180deg,#f4b088,#d07040)"></div><h4>JOHN SMITH</h4><p>Senior Vice President and General Manager</p></div>
<div class="member" style="top:3717px;left:843px"><div class="art" role="img" aria-label="Portrait photo of a team member" style="background:radial-gradient(ellipse 40% 55% at 50% 70%,#1a1a1a,transparent 80%),linear-gradient(180deg,#6a6a6a,#2a2a2a)"></div><h4>JOHN SMITH</h4><p>Senior Vice President and General Manager</p></div>

<!-- Awards -->
<div class="abs awards-label">HUGE HONOR</div>
<div class="abs awards-title">Our Awards</div>
<p class="abs awards-copy">Euismod in pellentesque massa placerat duis ultricies. Tristique nulla aliquet enim tortor at auctor urna nunc. Vel risusmodo viverra maecenas accumsan lacus vel facilisis volutpat. Leo urna molestie at elementum. Neque ornare aenean.</p>
<div class="award-row" style="top:4208px"><span style="left:4px">Ferrara Music Awards</span><span style="left:333px">Winner</span><span style="right:30px">2021</span></div>
<div class="award-row" style="top:4276px"><span style="left:4px">Meridian Song Festival Awards</span><span style="left:333px">Silver Award</span><span style="right:30px">2020</span></div>
<div class="award-row" style="top:4344px"><span style="left:4px">Open Stage Music Awards</span><span style="left:333px">Semi-Finalist</span><span style="right:30px">2019</span></div>
<div class="award-row" style="top:4412px"><span style="left:4px">Westside Remix Fest</span><span style="left:333px">Silver Award</span><span style="right:30px">2019</span></div>

<!-- Contact -->
<div class="abs contact-title">Lorem Ipsum is simply dummy text of the printing</div>
<p class="abs contact-copy">Lorem Ipsum is simply dummy text of the printing and typesetting industry. Lorem Ipsum has been the industry's standard dummy text ever since the 1500s, when an unknown printer took a galley of type and scrambled it to make a type specimen book.</p>

<footer class="abs footer"></footer>

<form class="abs form-box">
  <h3>Get in touch</h3>
  <div class="field" style="top:118px;left:40px;width:207px;height:48px">Name:</div>
  <div class="field" style="top:118px;left:262px;width:208px;height:48px">Phone:</div>
  <div class="field" style="top:193px;left:40px;width:207px;height:46px">Email:</div>
  <div class="field" style="top:193px;left:262px;width:208px;height:46px">Address:</div>
  <div class="field" style="top:266px;left:40px;width:430px;height:99px">Comments:</div>
  <div class="submit">Submit Now</div>
</form>

<div class="abs foot-tag">We create &amp; process<br>musical pieces</div>
<div class="abs vrule" style="left:507px"></div>
<div class="abs vrule" style="left:837px"></div>
<div class="abs foot-h" style="top:5054px;left:608px">Address</div>
<div class="abs foot-t" style="top:5092px;left:608px;width:210px">48 Larkspur Avenue,<br>Burbank, California 91502,<br>United States</div>
<div class="abs foot-h" style="top:5054px;left:903px">Say Hello</div>
<div class="abs foot-t" style="top:5092px;left:903px;font-size:12.5px">hello@reelhouseaudio.example</div>
<div class="abs" style="top:5116px;left:903px;font-size:21px;font-weight:700;color:var(--blue)">555-014-2290</div>
<div class="abs" style="top:5163px;left:904px;display:flex;gap:10px" aria-label="Social links">
  <span style="width:14px;height:14px;border-radius:50%;background:var(--blue)"></span>
  <span style="width:14px;height:14px;border-radius:50%;background:var(--white)"></span>
  <span style="width:14px;height:14px;border-radius:50%;background:var(--white)"></span>
</div>
<div class="abs foot-nav"><span>HOME</span><span>PEOPLE</span><span>SERVICES</span><span>PROJECT</span><span>LATEST</span><span>CONTACT US</span></div>
<div class="abs copyright">REELHOUSE AUDIO &copy; 2024. ALL RIGHTS RESERVED.</div>
<div class="abs to-top"><svg width="10" height="10" viewBox="0 0 10 10"><path d="M1.5 6.5 5 3l3.5 3.5" stroke="#fff" stroke-width="1.6" fill="none"/></svg></div>

</body>
</html>
```